card design for engineering consultancy

engineering drafting and project management company the provides drafting services for.
Electrical, Hydraulic, Mechanical, and Civil services
The company is called Q7R Services and logo is as attached
Information on card should be.
1. Logo
2.website : Q7RServices.example
3. email : info@Q7RServices.example
4. Phone: (+61) 400512836
5. Motto: Design - Document - Develop - Deliver

this card should be basically used for business identification only

Target Market(s)

electricians plumbers air conditioning installers and civil contractors

Industry/Entity Type

engineering, drafting, electrical, plumbing, airconditioning, civil

Contact Information for Business Card

1. Logo 2.website : Q7RServices.example 3. email : info@Q7RServices.example 4. Phone: (+61) 400512836 5. Motto: Design - Document - Develop - Deliver

Font styles to use
Serif

Requirements
Must have
• logo
Nice to have
• something inovative and different that makes it stand out from being just another business card

```html
<!DOCTYPE html>
<html lang="en">
<head>
<meta charset="utf-8">
<title>Q7R Services – Business Card</title>
<link rel="stylesheet" href="https://fonts.googleapis.com/css2?family=Montserrat:wght@400;500;700;800&family=Oswald:wght@500;600&display=swap">
<style>
  :root {
    --backdrop: #2b2b2b;
    --card-dark: #4a4a4a;
    --card-light: #ffffff;
    --ink: #4a4a4a;
    --ink-soft: #555555;
    --accent: #d1343c;
    --white: #ffffff;
  }
  * { box-sizing: border-box; margin: 0; padding: 0; }
  html, body {
    width: 1200px; height: 998px; overflow: hidden;
    background: var(--backdrop);
  }
  .canvas {
    position: relative; width: 1200px; height: 998px;
    display: flex; flex-direction: column; align-items: center;
    justify-content: center; gap: 70px;
  }
  .card {
    position: relative; width: 720px; height: 411px;
    overflow: hidden; border-radius: 2px;
    box-shadow: 0 14px 30px rgba(0,0,0,.45);
  }

  /* Back of card */
  .card--back { background: var(--card-dark); }
  .card--back .brand {
    position: absolute; left: 0; right: 0; top: 120px;
    display: flex; align-items: center; justify-content: center; gap: 16px;
  }
  .brand__mark { width: 26px; height: 26px; background: var(--accent); flex: none; }
  .brand__name {
    font-family: "Montserrat", sans-serif; font-weight: 800;
    font-size: 50px; letter-spacing: 5px; text-transform: uppercase;
    white-space: nowrap;
  }
  .card--back .brand__name { color: var(--white); }
  .services {
    position: absolute; left: 0; right: 0; bottom: 80px; text-align: center;
    font-family: "Oswald", sans-serif; font-weight: 600; font-size: 25px;
    color: var(--white); letter-spacing: .3px; text-transform: uppercase;
    white-space: nowrap;
  }
  .services .sep { margin: 0 10px; }

  /* Front of card */
  .card--front { background: var(--card-light); }
  .card--front .brand {
    position: absolute; left: 36px; top: 142px;
    display: flex; align-items: center; gap: 12px;
  }
  .card--front .brand__name { color: var(--ink); font-size: 28px; letter-spacing: 2px; }
  .card--front .brand__mark { width: 18px; height: 18px; }
  .divider {
    position: absolute; left: 360px; top: 44px; width: 2px; height: 230px;
    background: var(--accent);
  }
  .contact {
    position: absolute; left: 390px; top: 44px;
    font-family: "Montserrat", sans-serif; color: var(--ink-soft);
  }
  .contact__name {
    color: var(--accent); font-weight: 800; font-size: 30px;
    text-transform: uppercase; letter-spacing: .5px; line-height: 1;
    white-space: nowrap;
  }
  .contact__role { font-size: 17px; margin-top: 6px; }
  .contact__list { list-style: none; margin-top: 14px; }
  .contact__list li {
    display: flex; align-items: center; gap: 14px;
    font-size: 17px; line-height: 30px; white-space: nowrap;
  }
  .contact__list svg { width: 16px; height: 16px; flex: none; }
  .contact__address { font-size: 17px; line-height: 26px; margin-top: 14px; }

  .footer-bar {
    position: absolute; left: 0; bottom: 0; width: 720px; height: 70px;
  }
  .motto {
    position: absolute; left: 428px; right: 0; top: 357px; height: 46px;
    display: flex; align-items: center; justify-content: center;
    font-family: "Oswald", sans-serif; font-weight: 500; font-size: 15px;
    color: var(--white); text-transform: uppercase; letter-spacing: .3px;
    white-space: nowrap;
  }
</style>
</head>
<body>
<main class="canvas">

  <section class="card card--back" aria-label="Card back">
    <div class="brand">
      <span class="brand__mark"></span>
      <span class="brand__name">Q7R Services</span>
    </div>
    <p class="services">
      Electrical<span class="sep">|</span>Hydraulic<span class="sep">|</span>Mechanical and Civil Services
    </p>
  </section>

  <section class="card card--front" aria-label="Card front">
    <div class="brand">
      <span class="brand__mark"></span>
      <span class="brand__name">Q7R Services</span>
    </div>

    <div class="divider"></div>

    <div class="contact">
      <h1 class="contact__name">Daniel Harper</h1>
      <p class="contact__role">Managing Director</p>
      <ul class="contact__list">
        <li>
          <svg viewBox="0 0 16 16" aria-hidden="true"><path fill="var(--accent)" d="M3.6 1.5l2.2 2.6-1.3 1.6c.9 2 2.5 3.6 4.4 4.4l1.6-1.3 2.6 2.2-1.2 2.2C6.9 14.7 1.3 9.1 1.4 2.7z"/></svg>
          (+61) 400512836
        </li>
        <li>
          <svg viewBox="0 0 16 16" aria-hidden="true"><rect x="1" y="3" width="14" height="10" fill="var(--accent)"/><path d="M1 3.5l7 5 7-5" fill="none" stroke="#fff" stroke-width="1.2"/></svg>
          info@Q7RServices.example
        </li>
        <li>
          <svg viewBox="0 0 16 16" aria-hidden="true"><circle cx="8" cy="8" r="7" fill="var(--accent)"/><path d="M1 8h14M8 1c-3 3.5-3 10.5 0 14M8 1c3 3.5 3 10.5 0 14" fill="none" stroke="#fff" stroke-width="1"/></svg>
          www.Q7RServices.example
        </li>
      </ul>
      <p class="contact__address">421, Address line here<br>Country Name, 45452</p>
    </div>

    <svg class="footer-bar" viewBox="0 0 720 70" aria-hidden="true">
      <polygon points="0,48 400,48 396,56 0,56" fill="var(--accent)"/>
      <polygon points="0,62 400,62 422,16 720,16 720,70 0,70" fill="var(--ink)"/>
    </svg>
    <p class="motto">Design - Document - Develop - Deliver</p>
  </section>

</main>
</body>
</html>
```